New Managed IT company needs a business card

We are an IT management and support company that needs a business card design. I have a logo that I'll provide. Blues and blacks match the logo, but i'm open to anything. I want the card to help people take us seriously, but still have some energy and fun in it. The card should communicate stability and a solid company.

Target Market(s)

Target market includes Owners and Presidents at small businesses of 20 - 100 employees in the Pittsburgh PA area.

Industry/Entity Type

Information Technology

Contact Information for Business Card

i am open to other designs, but i imagine having only the logo on one side and then the logo plus all contact details on the other side.

Requirements
Must have
• Our logo
• Company name is optional if the logo makes it obvious
• A name - Lew Tasker
• A title - President
• A phone number - 555-XXX-XXXX
• A mobile phone number - 555-516-0471
• An email address - ltasker@brightlanetech.com
• a website - brightlanetech.com or www.brightlanetech.com
Nice to have
• some people tell me the logo feels like a superhero theme, some fun with that idea might be good. I'm open to ideas.
Should not have
• stock photos of people or computers - especially old looking stuff.

```html
<!DOCTYPE html>
<html lang="en">
<head>
<meta charset="utf-8">
<title>Bright Lane Tech — Business Card</title>
<link rel="stylesheet" href="https://fonts.googleapis.com/css2?family=Roboto:ital,wght@0,400;0,500;0,700;1,400&display=swap">
<style>
  :root {
    --bg: #2a2b2e;
    --blue: #0b94db;
    --blue-deep: #0d5f86;
    --blue-mid: #1a9fd6;
    --blue-light: #3bb7ea;
    --ink: #1d1f22;
    --rule: #3a3b3e;
    --white: #ffffff;
    --faint: #eef1f5;
  }
  * { box-sizing: border-box; margin: 0; padding: 0; }
  html, body {
    width: 1200px; height: 990px; overflow: hidden;
    background: var(--bg);
    font-family: "Roboto", Arial, sans-serif;
  }
  .canvas { position: relative; width: 1200px; height: 990px; }

  .card {
    position: absolute; left: 280px;
    width: 640px; height: 366px;
    border-radius: 24px; overflow: hidden;
    box-shadow: 0 14px 30px rgba(0,0,0,.45);
  }

  /* Back side */
  .card--back {
    top: 64px;
    background: radial-gradient(ellipse 60% 75% at 50% 48%, var(--blue-light) 0%, var(--blue-mid) 40%, var(--blue-deep) 100%);
    color: var(--white);
  }
  .card--back .brand {
    position: absolute; left: 0; right: 0; top: 120px;
    display: flex; align-items: center; justify-content: center; gap: 16px;
  }
  .card--back .brand-dot {
    width: 46px; height: 46px; border-radius: 50%; background: var(--white);
  }
  .card--back .brand-name {
    font-weight: 700; font-size: 40px; letter-spacing: 3px; text-transform: uppercase;
  }
  .card--back .site {
    position: absolute; left: 0; right: 0; top: 250px;
    text-align: center; font-size: 18px; letter-spacing: .3px;
  }

  /* Front side */
  .card--front { top: 536px; background: var(--white); }
  .card--front .top { position: absolute; inset: 0 0 auto 0; height: 168px; background: var(--white); }
  .card--front .rule { position: absolute; left: 0; right: 0; top: 168px; height: 8px; background: var(--rule); }
  .card--front .bottom {
    position: absolute; left: 0; right: 0; top: 176px; bottom: 0;
    background: linear-gradient(100deg, var(--blue) 0%, var(--blue) 40%, var(--blue-light) 52%, var(--blue) 66%, var(--blue) 100%);
  }
  .card--front .deco {
    position: absolute; right: -40px; top: 20px;
    width: 300px; height: 300px; border-radius: 50%;
    background: var(--faint); opacity: .7;
  }
  .card--front .brand {
    position: absolute; left: 40px; top: 54px;
    display: flex; align-items: center; gap: 14px;
  }
  .card--front .brand-dot { width: 44px; height: 44px; border-radius: 50%; background: var(--blue); }
  .card--front .brand-name {
    font-weight: 700; font-size: 34px; letter-spacing: 3px; text-transform: uppercase; color: var(--ink);
  }

  .contact {
    position: absolute; left: 40px; top: 200px;
    list-style: none; color: var(--white); font-size: 19px; line-height: 1.5;
  }
  .contact li { display: flex; align-items: center; gap: 12px; }
  .contact svg { width: 18px; height: 18px; flex: none; }

  .person { position: absolute; right: 40px; bottom: 40px; text-align: right; color: var(--white); }
  .person .name { font-weight: 700; font-size: 30px; }
  .person .title { font-size: 22px; margin-top: 2px; }
</style>
</head>
<body>
<main class="canvas">

  <section class="card card--back" aria-label="Card back">
    <div class="brand">
      <span class="brand-dot"></span>
      <span class="brand-name">Bright Lane Tech</span>
    </div>
    <p class="site">www.brightlanetech.com</p>
  </section>

  <section class="card card--front" aria-label="Card front">
    <div class="top"></div>
    <div class="deco"></div>
    <div class="rule"></div>
    <div class="bottom"></div>

    <div class="brand">
      <span class="brand-dot"></span>
      <span class="brand-name">Bright Lane Tech</span>
    </div>

    <ul class="contact">
      <li>
        <svg viewBox="0 0 24 24" aria-hidden="true"><circle cx="12" cy="12" r="11" fill="#fff"/><path d="M7 9c0-1 1-2 2-2h6c1 0 2 1 2 2v1h-3V9h-4v1H7z M8 11h8l1 5H7z" fill="#0b94db"/></svg>
        555-XXX-XXXX
      </li>
      <li>
        <svg viewBox="0 0 24 24" aria-hidden="true"><circle cx="12" cy="12" r="11" fill="#fff"/><rect x="9" y="5" width="6" height="14" rx="1.5" fill="#0b94db"/></svg>
        555-516-0471
      </li>
      <li>
        <svg viewBox="0 0 24 24" aria-hidden="true"><circle cx="12" cy="12" r="11" fill="#fff"/><rect x="6" y="8" width="12" height="8" fill="#0b94db"/><path d="M6 8l6 5 6-5" stroke="#fff" stroke-width="1.2" fill="none"/></svg>
        ltasker@brightlanetech.com
      </li>
      <li>
        <svg viewBox="0 0 24 24" aria-hidden="true"><circle cx="12" cy="12" r="11" fill="#fff"/><circle cx="12" cy="12" r="6" fill="none" stroke="#0b94db" stroke-width="1.5"/><path d="M6 12h12M12 6v12" stroke="#0b94db" stroke-width="1.2"/></svg>
        www.brightlanetech.com
      </li>
    </ul>

    <div class="person">
      <p class="name">Lew Tasker</p>
      <p class="title">President</p>
    </div>
  </section>

</main>
</body>
</html>
```